Business card design needed

We require business cards for our young and innovative construction team.

Our business is Brask Constructions and we have used Lime, Navy and white with our colours so far.

We would like business cards that show our passion for perfection and detail, communication and management.

Looking forward to seeing the deigns!!

Contact Information for Business Card

Dan Pellow
Brask Constructions Pty Ltd
PO Box 782 Quarrow Flats NSW 2795
Mobile: 0471 392 608
Email: dpellow@braskconstructions.com.au
Web: www.braskconstructions.com.au

```html
<!DOCTYPE html>
<html lang="en">
<head>
<meta charset="utf-8">
<title>Brask Constructions – Business Card</title>
<link href="https://fonts.googleapis.com/css2?family=Open+Sans:wght@400;600&family=Oswald:wght@500;600&display=swap" rel="stylesheet">
<style>
  :root {
    --page-bg: #2b2b2b;
    --navy: #34508a;
    --navy-light: #4a6aa8;
    --navy-dark: #2b4475;
    --lime: #7fbf2a;
    --card-white: #ffffff;
    --card-grey: #ececec;
    --text-grey: #6f6f6f;
    --rule-grey: #c9c9c9;
  }
  * { box-sizing: border-box; margin: 0; padding: 0; }
  html, body {
    width: 1200px; height: 901px; overflow: hidden;
    background: var(--page-bg);
  }
  .stage {
    position: relative; width: 1200px; height: 901px;
    display: flex; align-items: center; justify-content: center; gap: 60px;
  }
  .card {
    position: relative; width: 520px; height: 317px; overflow: hidden;
  }

  /* Front */
  .card--front {
    background: linear-gradient(180deg, var(--card-grey) 0%, var(--card-white) 45%, var(--card-white) 100%);
  }
  .front-band {
    position: absolute; inset: 0; width: 100%; height: 100%;
  }
  .brand {
    position: absolute; display: flex; align-items: center; gap: 10px;
    font-family: "Open Sans", sans-serif; font-weight: 600;
  }
  .brand__mark { display: block; flex: none; }
  .card--front .brand {
    left: 34px; top: 90px; color: var(--lime); font-size: 24px;
  }
  .card--front .brand__mark { width: 18px; height: 18px; background: var(--lime); }
  .holder-name {
    position: absolute; right: 70px; top: 112px;
    font-family: "Oswald", sans-serif; font-weight: 600;
    font-size: 24px; color: var(--navy-dark); letter-spacing: 0.5px;
  }
  .contact-list {
    position: absolute; left: 34px; top: 180px; list-style: none;
    font-family: "Open Sans", sans-serif; font-size: 13px;
    color: var(--text-grey); line-height: 22px;
  }
  .contact-list li { display: flex; align-items: center; gap: 10px; }
  .contact-list svg { width: 11px; height: 11px; fill: var(--lime); flex: none; }

  /* Back */
  .card--back {
    background: radial-gradient(ellipse at 45% 70%, var(--navy-light) 0%, var(--navy) 55%, var(--navy-dark) 100%);
    display: flex; flex-direction: column; align-items: center; justify-content: center;
  }
  .card--back .brand {
    position: static; color: var(--card-white); font-size: 42px; gap: 16px;
  }
  .card--back .brand__mark { width: 32px; height: 32px; background: var(--card-white); }
  .tagline {
    margin-top: 22px;
    font-family: "Oswald", sans-serif; font-weight: 500;
    font-size: 16px; color: var(--card-white); letter-spacing: 0.3px;
  }
</style>
</head>
<body>
<main class="stage">

  <section class="card card--front" aria-label="Business card front">
    <svg class="front-band" viewBox="0 0 520 317" preserveAspectRatio="none" aria-hidden="true">
      <line x1="0" y1="152" x2="470" y2="152" stroke="var(--rule-grey)" stroke-width="1"/>
      <polygon points="470,148 520,140 520,317 360,317" fill="var(--navy)"/>
    </svg>

    <div class="brand"><span class="brand__mark"></span>Brask Constructions</div>
    <div class="holder-name">Dan Pellow</div>

    <ul class="contact-list">
      <li>
        <svg viewBox="0 0 12 12"><rect x="3" y="0" width="6" height="12" rx="1.5"/></svg>
        0471 392 608
      </li>
      <li>
        <svg viewBox="0 0 12 12"><rect x="0" y="2" width="12" height="8" rx="1"/></svg>
        dpellow@braskconstructions.com.au
      </li>
      <li>
        <svg viewBox="0 0 12 12"><circle cx="6" cy="6" r="5.5"/></svg>
        www.braskconstructions.com.au
      </li>
      <li>
        <svg viewBox="0 0 12 12"><path d="M6 0a4 4 0 0 1 4 4c0 3-4 8-4 8S2 7 2 4a4 4 0 0 1 4-4z"/></svg>
        PO Box 782 Quarrow Flats NSW 2795
      </li>
    </ul>
  </section>

  <section class="card card--back" aria-label="Business card back">
    <div class="brand"><span class="brand__mark"></span>Brask Constructions</div>
    <p class="tagline">Brask Construction is a residential construction company</p>
  </section>

</main>
</body>
</html>
```